New Business Card Design Project

Make a kick ass business card for the Otter Cider Mug, using the designs. I also might like the 2nd place design logo on the back? Maybe all black with that? Not sure. Also, I'm cool with it being on metal, plastic, glass? or whatever for the business card. Maybe shaped like a shark? Let me know what else you need? Would like designs in the next day or so. Thank you.
Target Market(s)
Anyone that is cool
Contact Information for Business Card
Name: Daniel Forsby
Phone: 480.317.4962
inventor/creator/entrepreneur/owner
www.theottercidermug.example
social media links
https://www.facebook.com/theottercidermug
https://twitter.com/otter_cider
https://www.instagram.com/theottercidermug/
I'll get the Pinterest one soon
Colors
Designer to choose colors to be used in the design.
Requirements
Must have
- The Otter Cider Mug
- www.theottercidermug.example
- social media tags?
- My logos and picture/photo of wine glass
Nice to have
- Maybe shaped like a wine glass or shark
- I'll let you decide but my same colors from my website would be nice

```html
<!DOCTYPE html>
<html lang="en">
<head>
<meta charset="utf-8">
<title>Otter Cider Mug – Business Card</title>
<link rel="stylesheet" href="https://fonts.googleapis.com/css2?family=Open+Sans:wght@300;400;700&display=swap">
<style>
  :root {
    --backdrop: #2a2a2a;
    --card: #ffffff;
    --wine: #b3203a;
    --mauve: #a24d6e;
    --ink: #5a5a5a;
    --glass-grey: #e2e2e2;
    --dot-deep: #7a1f3d;
    --dot-rose: #c2506a;
    --dot-plum: #9a5a80;
  }
  * { margin: 0; padding: 0; box-sizing: border-box; }
  html, body {
    width: 1200px; height: 900px; overflow: hidden;
    background: var(--backdrop);
    font-family: "Open Sans", Arial, sans-serif;
  }
  .sheet {
    width: 1200px; height: 900px;
    display: flex; flex-direction: column; align-items: center; justify-content: center;
    gap: 36px;
  }
  .card {
    position: relative;
    width: 700px; height: 400px;
    background: var(--card);
    overflow: hidden;
    box-shadow: 0 10px 30px rgba(0,0,0,.45);
  }

  /* Front */
  .glass-art {
    position: absolute; left: 80px; top: 50px;
    width: 190px; height: 300px;
    background: linear-gradient(180deg, #eeeeee 0%, var(--glass-grey) 100%);
    border-radius: 90px 90px 10px 10px;
  }
  .front-brand {
    position: absolute; right: 60px; top: 150px;
    width: 320px;
    text-align: center;
  }
  .wordmark {
    font-weight: 300; font-size: 36px; color: var(--ink);
    letter-spacing: .5px;
    display: flex; align-items: center; justify-content: center; gap: 12px;
    white-space: nowrap;
  }
  .wordmark .mark-dot {
    width: 14px; height: 14px; border-radius: 50%; background: var(--wine);
    flex: none;
  }
  .social {
    display: flex; justify-content: center; gap: 6px; margin-top: 10px;
    list-style: none;
  }
  .social li {
    width: 22px; height: 22px; border-radius: 50%;
    background: var(--wine);
  }

  /* Back */
  .contact {
    position: absolute; left: 40px; top: 90px; width: 520px;
    text-align: center;
  }
  .contact .brand-name {
    font-weight: 400; font-size: 22px; color: var(--wine);
    margin-bottom: 8px;
  }
  .contact .person {
    font-weight: 700; font-size: 26px; color: var(--wine); line-height: 1.2;
  }
  .contact .roles {
    font-size: 17px; color: var(--mauve); margin-top: 4px;
  }
  .contact .details {
    font-size: 16px; color: var(--ink); margin-top: 4px;
  }
  .contact a { color: inherit; text-decoration: none; }
  .bubble-band {
    position: absolute; left: 0; bottom: 0; width: 700px; height: 230px;
    background: linear-gradient(90deg, var(--dot-rose) 0%, var(--dot-deep) 45%, var(--dot-plum) 75%, var(--wine) 100%);
    clip-path: polygon(0 100%, 0 88%, 14% 80%, 22% 62%, 34% 70%, 46% 56%, 58% 50%, 66% 36%, 74% 30%, 84% 24%, 92% 6%, 100% 0, 100% 100%);
    opacity: .85;
  }
</style>
</head>
<body>
<main class="sheet">
  <section class="card card-front">
    <div class="glass-art" role="img" aria-label="Faint grey illustration of a cider mug with the brand symbol inside"></div>
    <div class="front-brand">
      <div class="wordmark"><span class="mark-dot"></span>Otter Cider Mug</div>
      <ul class="social" aria-label="Social profiles">
        <li aria-label="Social profile one"></li>
        <li aria-label="Social profile two"></li>
        <li aria-label="Social profile three"></li>
      </ul>
    </div>
  </section>

  <section class="card card-back">
    <div class="contact">
      <p class="brand-name">Otter Cider Mug</p>
      <h1 class="person">Daniel Forsby</h1>
      <p class="roles">Inventor | Creator | Entrepreneur | Owner</p>
      <p class="details">480.317.4962 | <a href="https://www.theottercidermug.example">www.theottercidermug.example</a></p>
    </div>
    <div class="bubble-band" role="img" aria-label="Decorative scatter of wine, rose and plum coloured bubbles rising along the bottom edge"></div>
  </section>
</main>
</body>
</html>
```